Varemo Group Business Card Design

The CEO is looking for a new trendy look for his business card.
You can stay with current branding or come up with something new/creative. It can be 3D, including Medical Office buildings. You can use our logo in a variety of colors. Please include name, title, company name, company website, email address, cell number

Target Market(s)

Real Estate Development and Construction

Industry/Entity Type

Health care real estate

Contact Information for Business Card

Rohesh Kumbar, CEO M-727.418.9062 E-roheshkumbar@varemo.com Address:4100 Lindell Ave, Tampa, FL 33611 www.varemo.com

Font styles to use
Other font styles liked:
• Be creative

Requirements
Must have
• Creative, trendy look
Nice to have
• Please go to our website to get a feel- www. varemo.com
Should not have
• small fonts

```html
<!DOCTYPE html>
<html lang="en">
<head>
<meta charset="utf-8">
<title>Varemo Group Business Card</title>
<link href="https://fonts.googleapis.com/css2?family=Montserrat:wght@500;800&display=swap" rel="stylesheet">
<style>
  :root {
    --brand-red: #b01e28;
    --brand-red-light: #c9303a;
    --brand-red-dark: #8e161e;
    --navy: #1d2b4c;
    --paper: #ffffff;
    --backdrop: #8b8b8e;
  }
  * { margin: 0; padding: 0; box-sizing: border-box; }
  html, body { width: 900px; height: 1200px; overflow: hidden; }
  body {
    background: var(--backdrop);
    font-family: "Montserrat", Arial, sans-serif;
    position: relative;
  }
  .card {
    position: absolute;
    left: 134px;
    width: 633px;
    height: 364px;
    overflow: hidden;
  }
  .card--front { top: 210px; }
  .card--back { top: 624px; background: var(--paper); }

  .front-pattern {
    position: absolute;
    inset: 0;
    background: linear-gradient(100deg, var(--brand-red-dark) 0%, var(--brand-red) 45%, var(--brand-red-light) 100%);
  }
  .front-name {
    position: absolute;
    left: 0; right: 0;
    top: 168px;
    text-align: center;
    color: var(--paper);
    font-weight: 800;
    font-size: 34px;
    letter-spacing: -0.5px;
  }

  .company-name {
    position: absolute;
    right: 339px;
    top: 128px;
    text-align: right;
    color: var(--brand-red);
    font-weight: 800;
    font-size: 42px;
    line-height: 1;
    letter-spacing: -1px;
  }
  .divider {
    position: absolute;
    left: 316px;
    top: 94px;
    width: 2px;
    height: 178px;
    background: var(--navy);
  }
  .contact {
    position: absolute;
    left: 337px;
    top: 94px;
    color: var(--navy);
    font-weight: 500;
    font-size: 16.5px;
    line-height: 26px;
  }
  .contact__name {
    color: var(--brand-red);
    font-weight: 800;
    font-size: 27px;
    line-height: 32px;
  }
  .contact__row { display: flex; align-items: center; gap: 7px; }
  .contact__row svg { width: 13px; height: 13px; flex: none; fill: var(--brand-red); }
  .contact__phone { letter-spacing: 1.5px; }

  .band { position: absolute; bottom: 0; height: 12px; }
  .band--red { left: 0; width: 513px; background: var(--brand-red); }
  .band--navy { left: 516px; right: 0; background: var(--navy); }
</style>
</head>
<body>
  <section class="card card--front">
    <div class="front-pattern" role="img" aria-label="Red background with faint repeated company name pattern"></div>
    <div class="front-name">Varemo Group</div>
  </section>

  <section class="card card--back">
    <div class="company-name">Varemo<br>Group</div>
    <div class="divider"></div>
    <div class="contact">
      <div class="contact__name">Rohesh Kumbar</div>
      <div>CEO</div>
      <div>4100 Lindell Ave,</div>
      <div>Tampa, FL 33611</div>
      <div class="contact__row">
        <svg viewBox="0 0 16 16" aria-hidden="true"><path d="M3.5 1l2.5 3-1.5 1.8c.8 1.9 2.3 3.5 4.2 4.3L10.5 8.6 14 11l-1.3 3C7 14 2 9 2 2.6z"/></svg>
        <span class="contact__phone">727.418.9062</span>
      </div>
      <div class="contact__row">
        <svg viewBox="0 0 16 16" aria-hidden="true"><path d="M1 3h14v10H1z M1.8 4L8 9l6.2-5z" fill-rule="evenodd"/></svg>
        <span>roheshkumbar@varemo.com</span>
      </div>
      <div class="contact__row">
        <svg viewBox="0 0 16 16" aria-hidden="true"><path d="M8 1a7 7 0 100 14A7 7 0 008 1zm0 1.4c.9 1 1.5 2.4 1.7 4.1H6.3C6.5 4.8 7.1 3.4 8 2.4zM2.5 7.5h2.4c.1-1.6.6-3 1.3-4.2A5.6 5.6 0 002.5 7.5zm0 1h2.4c.1 1.6.6 3 1.3 4.2a5.6 5.6 0 01-3.7-4.2zm3.8 0h3.4c-.2 1.7-.8 3.1-1.7 4.1-.9-1-1.5-2.4-1.7-4.1zm4.8 0h2.4a5.6 5.6 0 01-3.7 4.2c.7-1.2 1.2-2.6 1.3-4.2zm0-1c-.1-1.6-.6-3-1.3-4.2a5.6 5.6 0 013.7 4.2z"/></svg>
        <span>www.varemo.com</span>
      </div>
    </div>
    <div class="band band--red"></div>
    <div class="band band--navy"></div>
  </section>
</body>
</html>
```